IT Recruitment Brochure

5 page brochure to promote our company's entrance into the Recruitment field
Target Market(s)
IT Professionals
Industry/Entity Type
It Company
Requirements
Must have
- 5 pages
quandrell silver partner logo
skelvor partner logo
plixon partner logo
obelu partner logo

```html
<!DOCTYPE html>
<html lang="en">
<head>
<meta charset="utf-8">
<title>Corevia Talent – IT Recruitment Brochure</title>
<link href="https://fonts.googleapis.com/css2?family=Arimo:wght@400;700&family=Tinos:wght@700&display=swap" rel="stylesheet">
<style>
:root{
  --backdrop:#f2f4f3;
  --paper:#ffffff;
  --lime:#aaff00;
  --green:#22dd00;
  --green-bright:#55ff00;
  --ink:#000000;
  --white:#ffffff;
  --head-green:#44cc00;
  --photo-a:#c9ccc9;
  --photo-b:#8a7a6c;
}
*{box-sizing:border-box;margin:0;padding:0}
html,body{width:1200px;height:900px;overflow:hidden;background:var(--backdrop);font-family:"Arimo",Arial,sans-serif}
.page{position:absolute;left:282px;top:0;width:636px;height:900px;background:var(--paper);box-shadow:0 0 24px rgba(0,0,0,.12)}
.block{position:absolute}
.label{position:absolute;display:flex;align-items:center;justify-content:center}
.label span{writing-mode:vertical-rl;transform:rotate(180deg);font-family:"Tinos","Times New Roman",serif;font-weight:700;font-size:14px;white-space:nowrap}

.photo{left:0;top:0;width:219px;height:225px;background:linear-gradient(135deg,var(--photo-a) 0%,#b8aca0 45%,var(--photo-b) 100%)}
.about-label{left:219px;top:0;width:39px;height:225px;background:var(--green);color:var(--white)}
.about{left:258px;top:0;width:378px;height:225px;background:var(--lime);color:var(--white);padding:48px 16px 0 18px;font-size:9.6px;line-height:12.6px;font-weight:700;text-align:justify}

.help-label{left:0;top:225px;width:38px;height:225px;background:var(--paper);color:var(--ink)}
.services{left:38px;top:225px;width:181px;height:225px;background:var(--green-bright);padding:18px 10px 0 21px;list-style:none}
.services li{color:var(--white);font-size:12px;line-height:13px;margin-bottom:12.5px}
.guarantee-label{left:219px;top:225px;width:39px;height:225px;background:var(--ink);color:var(--white)}
.guarantee{left:275px;top:245px;width:345px;display:flex;gap:11px}
.guarantee .col{width:156px;font-size:9.6px;line-height:12.3px;text-align:justify}
.guarantee .col:last-child{width:156px}
.promise-title{color:var(--head-green);font-size:12px;font-weight:700;line-height:14px}
.promise{margin-bottom:10px}
.note{font-size:7.2px;font-style:italic;margin-top:14px}

.method-label{left:0;top:450px;width:38px;height:225px;background:var(--green);color:var(--white)}
.method{left:38px;top:450px;width:598px;height:225px;background:var(--lime);padding:14px 18px 0 20px}
.method .intro{font-size:9.6px;line-height:12.6px;font-weight:700;color:var(--ink)}
.steps{display:flex;gap:11px;margin-top:11px}
.step{width:129px;color:var(--white);font-size:9.4px;line-height:11.4px}
.step b{color:var(--ink);font-weight:400;font-size:12px;text-transform:uppercase}

.cred-label{left:0;top:675px;width:38px;height:225px;background:var(--ink);color:var(--white)}
.credentials{left:57px;top:693px;width:545px;font-size:9.8px;line-height:12.8px;color:var(--ink)}
.partners{left:57px;top:815px;width:420px;height:40px;display:flex;align-items:center;justify-content:space-between}
.partner{display:flex;align-items:center;gap:6px;font-size:16px;font-weight:700;color:#1a1a1a}
.partner .mark{width:14px;height:14px;background:var(--head-green)}
.partner .dot{width:14px;height:14px;border-radius:50%;background:#1a3aa0}
.partner.blue{color:#1a3aa0}
.partner.red .mark{background:#d3202e}
.partner.red{color:#1a1a1a}
</style>
</head>
<body>
<main class="page">
  <div class="block photo" role="img" aria-label="Photo of many hands stacked together in a team gesture"></div>
  <div class="label about-label"><span>About us</span></div>
  <section class="block about">
    <p>Corevia Talent has been in I.T. Training and Certifications for the past 3 years. Our growth has been fuelled by the growth in the I.T. sector which is on track for greater growth than ever. Throughout this time, we have successfully trained and placed many candidates who now are well placed in the job market. Today, business and market dynamics are moving rapidly and continuously and along with it, strategies and technologies are changing too. Talent and time are short in supply and nearly in all fields, skilled people are hard to find. To cater for such change, gap and overwhelming growth, Corevia Talent has setup a dedicated I.T. Recruitment arm. Here we combine the input from the employers and design and deliver training to our candidates hence making the best match for employers and employees.</p>
  </section>

  <div class="label help-label"><span>What we can help you with?</span></div>
  <ul class="block services">
    <li>Temporary Staff</li>
    <li>Contract Staff</li>
    <li>Permanent Staff</li>
    <li>Staff training and Certifications</li>
  </ul>
  <div class="label guarantee-label"><span>What we Guarantee?</span></div>
  <section class="block guarantee">
    <div class="col">
      <div class="promise">
        <h3 class="promise-title">QUALITY Promise:</h3>
        <p>At Corevia Talent we guarantee that our candidates will meet the best industry standards and client requirement.</p>
      </div>
      <div class="promise">
        <h3 class="promise-title">PRICE Promise:</h3>
        <p>Our prices are the lowest in the entire industry. If you find a cheaper price, we will charge you nothing for our candidate. *</p>
      </div>
      <p class="note">*Please refer to the GSA for further details.</p>
    </div>
    <div class="col">
      <h3 class="promise-title">SERVICE Promise:</h3>
      <p>At Corevia Talent, we work with you to recruit staff specific to your business strategy and needs, enabling the candidate to perfectly align with the organisation. Therefore, we guarantee that if after employing our candidate you feel they are not up to the standard, we will work with you to overcome any difficulties, or as an alternative, replace that candidate with a candidate of your choice at no further cost. *</p>
    </div>
  </section>

  <div class="label method-label"><span>How we get it right?</span></div>
  <section class="block method">
    <p class="intro">At Corevia Talent we use a simple formula to guide our success, which is entirely dependent on the success of our client. Our emphasis lies on four key processes:</p>
    <div class="steps">
      <p class="step"><b>Identifying</b> the gap, the first and foremost step is to know what is required and where it is required. This lets us filter out all the noise surrounding our process letting us focus on the key aspect.</p>
      <p class="step"><b>Obtaining</b> talent is the next key step in our strategy. Finding applicants is easy, but finding the right applicant isn't, and we at Corevia Talent will guarantee finding you the right talent. We have a pool of applicants ranging from basic to critical IT roles and functions obtained from various sources.</p>
      <p class="step"><b>Assessing</b> our candidate is considered a core activity as it is vital in matching the candidate to the job opening. We assess our candidate on grounds such as education, technical skills, written and verbal communication skills and interpersonal skills.</p>
      <p class="step"><b>Managing</b> people, integrated with our skill to manage efficiently both client and candidate, we are able to offer both parties with a practical and efficient way in which to unleash their greatest potential.</p>
    </div>
  </section>

  <div class="label cred-label"><span>Our Credentials</span></div>
  <p class="block credentials">As portion of our business focuses on I.T. training and certifications, Corevia Talent is proving to be one of the best I.T. training institutes in Australia. We proudly claim that we are a Quandrell Silver Partner and the sole Authorised Skelvor Learning Partner in Victoria, a clear statement of our excellence!</p>
  <div class="block partners">
    <div class="partner"><span>Quandrell</span><span class="mark"></span></div>
    <div class="partner red"><span class="mark"></span><span>Skelvor</span></div>
    <div class="partner"><span>plixon</span></div>
    <div class="partner blue"><span class="dot"></span><span>obelu</span></div>
  </div>
</main>
</body>
</html>
```